IV Nutritional Clinic Web Design

We are working with Velmo. They are an IV Nutritional Clinic and in need of a new website design.
Some sites to use for inspiration:
https://brantlowcare.example
https://www.zolvarihealth.example
https://www.quellspa.example
https://pimrolift.example
https://www.dorvak-well.example/pages/iv-therapy-west-hollywood
https://www.tqoncowell.example/cancer-care/iv-drips/
https://drelmavita.example
https://salbrikmed.example
Thank you for taking the time to consider designing a website for us. We are web developers based in Stockton, CA, USA. Most of our projects go through the same process. Understanding this process may help you win a project with us. We custom-code all of our websites in-house. We don’t have any requirements as to what tools you use for your design, but we prefer Figma files. For any design that we label as four-stars, we send it to the client for review. The client picks the final design they want us to use. Once we complete this process, we will continue to show additional clients all the four-star sites and purchase them later. Your designs will have multiple chances to sell. For better chances of success, we ask that you follow these guidelines.
IMAGES:
If you use any images or icons in the design, we ask that you have a link to the asset so we can purchase the image/icon. Most of the designs we submit do not have the customer’s images on them unless they have some great images. Be creative; show us the feeling you are trying to portray with your image choices. Use any royalty-free site you choose. We subscribe to Corvix and mainly use their images, but we can purchase images outside of Corvix.
PLEASE NOTE: we will not submit designs to clients with watermarks on the images.
FONTS:
We ask that you identify the fonts used in the design. This can be done in a message if you want. We typically use Lumen Typeset and Corvix Fonts.
CONTENT:
We're always open to different content and ideas. We often submit designs with stock images so the client can see our vision. We typically take pictures after the website launch to use their images with our vision. Lorem Ipsum is fine for paragraphs, but we ask that you write the headers in correct English. We want to be able to show the vision and identify the sections of the website.
INSPIRATION:
We typically add a couple of links in the brief of websites we like to help you get started in your design.
REVISIONS:
We do not often ask for revisions of the designs unless we see something in the design that may not appeal to the client. If there are slight changes that we want to make, we do that in the development process.
FEEDBACK:
We rarely give feedback on designs during the design process. We are working on many website projects and do not have the time to provide feedback. We usually respond if your request is well thought out and asks specific questions, but a note asking “feedback, please” usually goes unanswered.
Number of Pages Required
1 page
Look and feel
Each slider illustrates characteristics of the customer's brand and the style your logo design should communicate.

```html
<!DOCTYPE html>
<html lang="en">
<head>
<meta charset="utf-8">
<title>Velmo Hydration – IV Nutrient Therapy</title>
<link href="https://fonts.googleapis.com/css2?family=Gilda+Display&family=Jost:wght@400;500;600&display=swap" rel="stylesheet">
<style>
:root{
  --navy:#1d2a86;
  --navy-dark:#1a247a;
  --green:#6e9c3c;
  --green-light:#8ab55a;
  --ink:#111;
  --line:#e3e6ee;
  --mint:#eaf5ea;
  --sky:#e3eff8;
  --white:#fff;
}
*{box-sizing:border-box;margin:0;padding:0}
html,body{width:1200px;height:4068px;overflow:hidden}
body{position:relative;font-family:"Jost",sans-serif;color:var(--ink);background:var(--white)}
.abs{position:absolute}
.serif{font-family:"Gilda Display",serif;color:var(--navy);font-weight:400}
.btn{position:absolute;display:flex;align-items:center;justify-content:center;background:var(--navy);color:#fff;border-radius:20px;font-size:14px;font-weight:500;text-decoration:none}
.ph{position:absolute}

/* header */
.site-header{position:absolute;left:0;top:0;width:1200px;height:118px;background:#fff}
.brand{position:absolute;left:57px;top:30px;display:flex;align-items:center;gap:10px}
.brand-name{font-family:"Jost",sans-serif;font-weight:600;font-size:40px;color:var(--navy);letter-spacing:1px}
.brand-dot{width:14px;height:14px;background:var(--green);border-radius:50%}
.nav{position:absolute;top:44px;left:614px;display:flex;gap:46px;font-size:19px;font-weight:500;color:#111}
.nav-contact{left:1046px;top:44px;width:98px;height:32px;font-size:19px}

/* hero */
.hero{position:absolute;left:0;top:118px;width:1200px;height:552px;overflow:hidden;background:linear-gradient(90deg,#eef5fb 0%,#e6f0f8 45%,#dde6ee 100%)}
.hero-photo{left:520px;top:0;width:680px;height:552px;background:linear-gradient(90deg,rgba(230,240,248,0) 0%,#c9d6e3 30%,#b9c6d6 70%,#8fa5c4 100%)}
.hero h1{position:absolute;left:57px;top:128px;font-size:51px;line-height:74px}
.hero p{position:absolute;left:57px;top:278px;width:440px;font-size:15px;line-height:19px}
.hero .btn{left:57px;top:366px;width:185px;height:32px}

/* about */
.about-photo{background:linear-gradient(135deg,#d8dee6,#aeb9c6)}
.about h2{position:absolute;left:671px;top:780px;font-size:52px}
.about p{position:absolute;left:669px;width:470px;font-size:11px;line-height:14.5px}
.about .btn{left:671px;top:1077px;width:118px;height:32px}

/* treatments */
.treatments{position:absolute;left:0;top:1208px;width:1200px;height:461px;background:linear-gradient(90deg,#e8f4ea,#f5faf5 50%,#e8f4ea)}
.treatments h2{position:absolute;width:1200px;top:50px;text-align:center;font-size:52px}
.t-card{position:absolute;width:354px;height:135px;background:#fff;border:1px solid var(--line);display:flex;align-items:center;padding-left:24px;gap:24px}
.t-icon{width:72px;height:72px;border-radius:50%;background:var(--green);display:flex;align-items:center;justify-content:center;flex:none}
.t-name{font-size:18px;font-weight:600;color:var(--navy)}

/* journey */
.journey h2{position:absolute;left:57px;top:1730px;font-size:52px;line-height:72px}
.journey p{position:absolute;left:632px;top:1759px;width:215px;font-size:11px;line-height:14px}
.journey .btn{left:632px;top:1825px;width:150px;height:31px}
.journey-photo{left:57px;top:1893px;width:783px;height:332px;background:linear-gradient(120deg,#c9cfc4,#e8ecef 45%,#a9c6d6)}
.stat{position:absolute;left:876px;width:266px;height:144px;border:1px solid var(--line);text-align:center}
.stat b{display:block;font-family:"Gilda Display",serif;font-weight:400;font-size:62px;color:var(--green);margin-top:24px;line-height:64px}
.stat span{font-size:24px;color:var(--navy);font-weight:500}

/* unlock */
.unlock{position:absolute;left:0;top:2286px;width:1200px;height:311px;background:linear-gradient(90deg,#d9eaf6,#eef5fa 50%,#d4e7f4)}
.unlock h2{position:absolute;width:1200px;top:54px;text-align:center;font-size:51px;line-height:73px}
.unlock .btn{left:504px;top:216px;width:192px;height:32px}

/* blogs */
.blogs-title{position:absolute;width:1200px;top:2655px;text-align:center;font-size:52px}
.b-card{position:absolute;top:2740px;width:354px;height:423px;border:1px solid var(--line);background:#fff}
.b-img{left:16px;top:15px;width:320px;height:146px;background:linear-gradient(135deg,#d7dde4,#b7c3ce)}
.b-date{position:absolute;left:16px;top:15px;background:var(--navy);color:#fff;font-size:12px;padding:3px 14px}
.b-card h3{position:absolute;left:16px;top:186px;width:320px;font-size:20px;line-height:30px}
.b-card p{position:absolute;left:16px;top:263px;width:320px;font-size:12.5px;line-height:16px}
.b-card .btn{left:16px;top:376px;width:150px;height:32px}

/* booking */
.booking{position:absolute;left:0;top:3226px;width:1200px;height:557px;background:linear-gradient(180deg,#e6f2e8,#eef6ef 60%,#e4f0e6)}
.booking h2{position:absolute;width:1200px;top:45px;text-align:center;font-size:52px}
.field{position:absolute;background:#fff;border:1px solid #cfd4dc;border-radius:18px;font-size:12px;color:#888;padding:0 16px;display:flex;align-items:center}
.booking .btn{left:257px;top:376px;width:686px;height:39px;font-size:15px}
.contact-item{position:absolute;top:466px;display:flex;align-items:center;gap:18px;font-size:15px;font-weight:500;line-height:18px}
.c-icon{width:34px;height:34px;border-radius:50%;background:var(--green);display:flex;align-items:center;justify-content:center;flex:none}

/* footer */
.site-footer{position:absolute;left:0;top:3783px;width:1200px;height:285px;background:var(--navy);color:#fff}
.f-brand{position:absolute;left:57px;top:64px;font-size:44px;font-weight:600;letter-spacing:1px}
.f-about{position:absolute;left:57px;top:154px;font-size:12.5px;line-height:15px;width:190px}
.f-col{position:absolute;top:56px}
.f-col h4{font-size:16px;font-weight:500;color:var(--green-light);margin-bottom:14px}
.f-col ul{list-style:none;font-size:12.5px;line-height:23px}
.f-col li::before{content:"▸";color:var(--green-light);margin-right:10px;font-size:10px}
.subscribe{position:absolute;left:925px;top:98px;width:216px;height:32px;display:flex}
.subscribe .in{flex:1;background:#fff;color:#777;font-size:12px;display:flex;align-items:center;padding-left:22px}
.subscribe .go{width:34px;background:var(--green);display:flex;align-items:center;justify-content:center}
.socials{position:absolute;left:925px;top:162px;display:flex;gap:10px}
.socials span{width:25px;height:25px;border-radius:50%;background:var(--green)}
.f-bar{position:absolute;left:0;top:239px;width:1200px;border-top:1px solid #3d49a0}
.f-copy{position:absolute;left:55px;top:252px;font-size:12.5px}
.f-legal{position:absolute;right:58px;top:252px;font-size:12.5px}
</style>
</head>
<body>

<header class="site-header">
  <div class="brand"><span class="brand-name">VELMO</span><span class="brand-dot"></span></div>
  <nav class="nav"><span>Home</span><span>About us</span><span>Services</span><span>Blogs</span></nav>
  <a class="btn nav-contact">Contact</a>
</header>

<section class="hero">
  <div class="ph hero-photo" role="img" aria-label="Nurse attending a relaxed patient receiving an IV drip in a bright clinic room"></div>
  <h1 class="serif">Elevate Your Wellness<br>with IV Nutrient Therapy</h1>
  <p>Lorem ipsum dolor sit amet, consectetuer adipiscing elit, sed diam nonummy nibh euismod tincidunt ut laoreet dolore magna aliquam erat volutpat.</p>
  <a class="btn">Book an appointment</a>
</section>

<section class="about">
  <div class="ph about-photo" style="left:57px;top:739px;width:253px;height:185px" role="img" aria-label="Family consulting a doctor at a desk"></div>
  <div class="ph about-photo" style="left:318px;top:739px;width:252px;height:185px" role="img" aria-label="Doctor checking on a patient in bed"></div>
  <div class="ph about-photo" style="left:57px;top:933px;width:297px;height:204px" role="img" aria-label="Nurse greeting a resting patient"></div>
  <div class="ph about-photo" style="left:364px;top:933px;width:206px;height:204px" role="img" aria-label="Smiling patient with a doctor"></div>
  <h2 class="serif">About Us</h2>
  <p style="top:856px">Lorem ipsum dolor sit amet, consectetuer adipiscing elit, sed diam nonummy nibh euismod tincidunt ut laoreet dolore magna aliquam erat volutpat. Ut wisi enim ad minim veniam, quis nostrud exerci tation ullamcorper suscipit lobortis nisl ut aliquip ex ea commodo</p>
  <p style="top:929px">consequat. Duis autem vel eum iriure dolor in hendrerit in vulputate velit esse molestie consequat, vel illum dolore eu feugiat nulla facilisis at vero eros et accumsan et iusto odio dignissim qui blandit praesent luptatum zzril delenit augue duis dolore te feugait nulla facilisi.</p>
  <p style="top:1003px">consequat. Duis autem vel eum iriure dolor in hendrerit in vulputate velit esse molestie consequat, vel illum dolore eu feugiat nulla facilisis</p>
  <a class="btn">Know More</a>
</section>

<section class="treatments">
  <h2 class="serif">IV Treatments</h2>
  <div class="t-card" style="left:57px;top:137px"><span class="t-icon"><svg width="36" height="36" viewBox="0 0 36 36" fill="none" stroke="#fff" stroke-width="2.5"><circle cx="18" cy="18" r="13"/><path d="M18 10v8l5 4"/></svg></span><span class="t-name">Anti-Aging Therapy</span></div>
  <div class="t-card" style="left:422px;top:137px"><span class="t-icon"><svg width="36" height="36" viewBox="0 0 36 36" fill="none" stroke="#fff" stroke-width="2.5"><circle cx="18" cy="16" r="11"/><path d="M14 27v5h8v-5"/></svg></span><span class="t-name">Brain Improvement IV</span></div>
  <div class="t-card" style="left:788px;top:137px"><span class="t-icon"><svg width="36" height="36" viewBox="0 0 36 36" fill="none" stroke="#fff" stroke-width="2.5"><path d="M18 6v24M6 18h24"/><circle cx="18" cy="18" r="13"/></svg></span><span class="t-name">Digestive IV</span></div>
  <div class="t-card" style="left:57px;top:283px"><span class="t-icon"><svg width="36" height="36" viewBox="0 0 36 36" fill="none" stroke="#fff" stroke-width="2.5"><rect x="11" y="7" width="14" height="20" rx="3"/><path d="M18 27v6"/></svg></span><span class="t-name">Energy Drip</span></div>
  <div class="t-card" style="left:422px;top:283px"><span class="t-icon"><svg width="36" height="36" viewBox="0 0 36 36" fill="none" stroke="#fff" stroke-width="2.5"><path d="M18 30 6 18a7 7 0 0 1 12-9 7 7 0 0 1 12 9z"/><path d="M9 18h6l2-4 3 7 2-3h5"/></svg></span><span class="t-name">Healthy Heart IV</span></div>
  <div class="t-card" style="left:788px;top:283px"><span class="t-icon"><svg width="36" height="36" viewBox="0 0 36 36" fill="none" stroke="#fff" stroke-width="2.5"><path d="M18 5l11 6v12l-11 7-11-7V11z"/></svg></span><span class="t-name">Skin Rejuvenation</span></div>
</section>

<section class="journey">
  <h2 class="serif">Your Journey to Better<br>Health Starts Here</h2>
  <p>Lorem ipsum dolor sitadipiscing elit, sed diam nonummy nibh euismod tincidunt</p>
  <a class="btn">Continue Reading</a>
  <div class="ph journey-photo" role="img" aria-label="Doctor and nurse welcoming a patient with a handshake"></div>
  <div class="stat" style="top:1764px"><b>96%</b><span>Recovered Patients</span></div>
  <div class="stat" style="top:1922px"><b>275k</b><span>Satisfaction Rate</span></div>
  <div class="stat" style="top:2080px"><b>86</b><span>Skilled Doctors</span></div>
</section>

<section class="unlock">
  <h2 class="serif">Unlock Your Wellness Potential<br>with IV Vitamin Therapy</h2>
  <a class="btn">Contact Now</a>
</section>

<section class="blogs">
  <h2 class="serif blogs-title">Blogs</h2>
  <article class="b-card" style="left:57px">
    <div class="ph b-img" role="img" aria-label="Senior woman relaxing during an IV drip"></div>
    <span class="b-date">March 01, 2024</span>
    <h3 class="serif">Experience the Benefits of IV Nutrient Therapy Drips</h3>
    <p>Lorem ipsum dolor sit amet, consectetuer adipiscing elit, sed diam nonummy nibh euismod tincidunt ut laoreet dolore magna aliquam erat volutpat. Ut wisi enim ad minim veniam, quis nostrud exerci tation ullamcorper suscipit lobortis nisl ut aliquip ex ea commodo</p>
    <a class="btn">Continue Reading</a>
  </article>
  <article class="b-card" style="left:422px">
    <div class="ph b-img" role="img" aria-label="Gloved hands adjusting an IV bag"></div>
    <span class="b-date">May 23, 2022</span>
    <h3 class="serif">Unlock Your Wellness Potential with IV Vitamin Therapy</h3>
    <p>Lorem ipsum dolor sit amet, consectetuer adipiscing elit, sed diam nonummy nibh euismod tincidunt ut laoreet dolore magna aliquam erat volutpat. Ut wisi enim ad minim veniam, quis nostrud exerci tation ullamcorper suscipit lobortis nisl ut aliquip ex ea commodo</p>
    <a class="btn">Continue Reading</a>
  </article>
  <article class="b-card" style="left:788px">
    <div class="ph b-img" role="img" aria-label="Two women talking in a plant-filled lounge"></div>
    <span class="b-date">March 06, 2020</span>
    <h3 class="serif">Discover IV Nutrient Therapy Drips Today</h3>
    <p>Lorem ipsum dolor sit amet, consectetuer adipiscing elit, sed diam nonummy nibh euismod tincidunt ut laoreet dolore magna aliquam erat volutpat. Ut wisi enim ad minim veniam, quis nostrud exerci tation ullamcorper suscipit lobortis nisl ut aliquip ex ea commodo</p>
    <a class="btn">Continue Reading</a>
  </article>
</section>

<section class="booking">
  <h2 class="serif">Book Your IV Vitamin Drip Session Now</h2>
  <div class="field" style="left:257px;top:144px;width:336px;height:35px">First Name</div>
  <div class="field" style="left:607px;top:144px;width:336px;height:35px">Last Name</div>
  <div class="field" style="left:257px;top:193px;width:336px;height:35px">E - Mail</div>
  <div class="field" style="left:607px;top:193px;width:336px;height:35px">Subject</div>
  <div class="field" style="left:257px;top:241px;width:686px;height:117px;align-items:flex-start;padding-top:14px">Message...</div>
  <a class="btn">Book Your IV Therapy Today</a>
  <div class="contact-item" style="left:272px">
    <span class="c-icon"><svg width="18" height="18" viewBox="0 0 24 24" fill="#fff"><path d="M6.6 10.8a15 15 0 0 0 6.6 6.6l2.2-2.2a1 1 0 0 1 1-.25 11 11 0 0 0 3.6.6 1 1 0 0 1 1 1V20a1 1 0 0 1-1 1A17 17 0 0 1 3 4a1 1 0 0 1 1-1h3.5a1 1 0 0 1 1 1 11 11 0 0 0 .6 3.6 1 1 0 0 1-.25 1z"/></svg></span>555 014 2987</div>
  <div class="contact-item" style="left:482px">
    <span class="c-icon"><svg width="18" height="18" viewBox="0 0 24 24" fill="#fff"><path d="M12 2a7 7 0 0 0-7 7c0 5 7 13 7 13s7-8 7-13a7 7 0 0 0-7-7zm0 9.5A2.5 2.5 0 1 1 12 6.5a2.5 2.5 0 0 1 0 5z"/></svg></span>Lorem ipsum dolor sit<br>amet, conse,&nbsp; 09873</div>
  <div class="contact-item" style="left:758px">
    <span class="c-icon"><svg width="18" height="18" viewBox="0 0 24 24" fill="#fff"><path d="M3 5h18v14H3z"/><path d="M3 5l9 7 9-7" stroke="#6e9c3c" stroke-width="2" fill="none"/></svg></span>info@velmo.example</div>
</section>

<footer class="site-footer">
  <div class="f-brand">VELMO</div>
  <p class="f-about">Lorem ipsum dolor sit amet, consectetuer adipiscing</p>
  <div class="f-col" style="left:368px"><h4>Quick links</h4><ul><li>Home</li><li>About us</li><li>Services</li><li>Blogs</li><li>Contact</li></ul></div>
  <div class="f-col" style="left:631px"><h4>IV Treatment</h4><ul><li>Energy Drip</li><li>Digestive IV</li><li>Skin Rejuvenation</li><li>Anti-Aging Therapy</li><li>Brain Improvement IV</li></ul></div>
  <div class="f-col" style="left:925px"><h4>Subscribe for news letter</h4></div>
  <div class="subscribe"><span class="in">Enter your mail</span><span class="go"><svg width="18" height="12" viewBox="0 0 18 12" fill="none" stroke="#fff" stroke-width="1.6"><path d="M1 6h15M11 1l5 5-5 5"/></svg></span></div>
  <div class="socials"><span></span><span></span><span></span><span></span></div>
  <div class="f-bar"></div>
  <p class="f-copy">Copyright © 2025 Velmo All rights reserved.</p>
  <p class="f-legal">Privacy Policy | Terms and Conditions</p>
</footer>

</body>
</html>
```